IT services company needs a business card designed

-2 sided business card.-Front is going to be the logo raised (3D floating effect) on a black background. Make the logos spider web shiny silver and keep the spider the same design. -Back needs to have the following information:Darrel Sotho, Managing Partner, Cell: 738-402-1954, Website: Plankhorn.com, Email: Darrel@Plankhorn.com
Target Market(s)
IT Services
Industry/Entity Type
It Company
Contact Information for Business Card
-2 sided business card.
-Front is going to be the logo raised (3D floating effect) on a black background. Make the logos spider web shiny silver and keep the spider the same design.
-Back needs to have the following information:
Darrel Sotho, Managing Partner, Cell: 738-402-1954, Website: Plankhorn.com, Email: Darrel@Plankhorn.com

```html
<!DOCTYPE html>
<html lang="en">
<head>
<meta charset="utf-8">
<title>Plankhorn Business Card</title>
<link href="https://fonts.googleapis.com/css2?family=Roboto:wght@300;400;500&display=swap" rel="stylesheet">
<style>
  :root {
    --page-bg: #efefef;
    --card-bg: #262626;
    --silver: #cfcfcf;
    --text-white: #ffffff;
    --icon-ink: #262626;
    --web-tone: #5a5a5a;
  }
  html, body {
    margin: 0;
    padding: 0;
    width: 1200px;
    height: 1200px;
    overflow: hidden;
    background: var(--page-bg);
    font-family: "Roboto", sans-serif;
  }
  .card {
    position: absolute;
    left: 168px;
    width: 863px;
    height: 506px;
    background: var(--card-bg);
    overflow: hidden;
  }
  .card--front { top: 63px; }
  .card--back { top: 634px; }

  .brand-name {
    position: absolute;
    left: 0;
    right: 0;
    top: 210px;
    text-align: center;
    font-weight: 300;
    font-size: 66px;
    letter-spacing: 4px;
    color: var(--silver);
    margin: 0;
    line-height: 1;
  }

  .person {
    position: absolute;
    left: 54px;
    top: 42px;
    color: var(--text-white);
  }
  .person__name {
    margin: 0;
    font-weight: 500;
    font-size: 35px;
    line-height: 1.1;
  }
  .person__title {
    margin: 6px 0 0;
    font-weight: 400;
    font-size: 27px;
    letter-spacing: 0.5px;
  }

  .contacts {
    position: absolute;
    left: 54px;
    top: 340px;
    margin: 0;
    padding: 0;
    list-style: none;
  }
  .contacts__item {
    display: flex;
    align-items: center;
    height: 45px;
    color: var(--text-white);
    font-size: 26px;
  }
  .contacts__icon {
    width: 28px;
    height: 28px;
    margin-right: 28px;
    flex: none;
  }

  .web-decoration {
    position: absolute;
    right: 0;
    top: 0;
    width: 245px;
    height: 506px;
    background: radial-gradient(ellipse at 100% 50%, var(--web-tone) 0%, rgba(90,90,90,0.35) 45%, rgba(38,38,38,0) 75%);
  }
</style>
</head>
<body>
  <section class="card card--front">
    <h1 class="brand-name">PLANKHORN</h1>
  </section>

  <section class="card card--back">
    <div class="person">
      <h2 class="person__name">Darrel Sotho</h2>
      <p class="person__title">Managing Partner</p>
    </div>

    <ul class="contacts">
      <li class="contacts__item">
        <svg class="contacts__icon" viewBox="0 0 28 28" aria-hidden="true">
          <circle cx="14" cy="14" r="14" fill="#fff"/>
          <path d="M9.5 7.5l3 3-1.6 1.8c.9 1.9 2.4 3.4 4.3 4.3l1.8-1.6 3 3-2 2.2C12.8 19.8 8.2 15.2 7.3 9.5z" fill="var(--icon-ink)"/>
        </svg>
        738-402-1954
      </li>
      <li class="contacts__item">
        <svg class="contacts__icon" viewBox="0 0 28 28" aria-hidden="true">
          <circle cx="14" cy="14" r="14" fill="#fff"/>
          <rect x="7" y="9" width="14" height="10" rx="1" fill="var(--icon-ink)"/>
          <path d="M7.5 9.5l6.5 5 6.5-5" stroke="#fff" stroke-width="1.4" fill="none"/>
        </svg>
        Darrel@Plankhorn.com
      </li>
      <li class="contacts__item">
        <svg class="contacts__icon" viewBox="0 0 28 28" aria-hidden="true">
          <circle cx="14" cy="14" r="14" fill="#fff"/>
          <path d="M10 7l9 8.5-4.2.4 2.4 4.6-1.8.9-2.4-4.6L10 19.6z" fill="var(--icon-ink)"/>
        </svg>
        www.Plankhorn.com
      </li>
    </ul>

    <div class="web-decoration" role="img" aria-label="Faint grey spider web decoration along the right edge"></div>
  </section>
</body>
</html>
```